Brellmoor Aviation Needs a New Website

1. Details about the company
The website is for a company that conducts businesses in Singapore, Africa and Australia. The name of the Company is Brellmoor.
The services include
• Aviation engineering services
• Aviation consulting
• Aviation equipment supplies
• Aviation construction projects
• Aviation business development
2. The designing
• The design can be custom design or premium template redesign
• The theme must be very classy and corporate
• Images to be used on the site must represent the services that the company conducts (5 images)
• The company logo is supplied to be used on the homepage and for the favicon
• The design to be installed on www.brellmoor-example.com
3. The Pages
There will be 5 pages.
a. Home
• With latest news widget (showing the 3 latest news)
• Facebook, Twitter links
b. About us
c. News
• Weekly news will be posted on this page and the latest news widget will be shown on the homepage
d. Services
• With Request-for-a-quote plugin
e. Contact Us
• Phone numbers
• Fax numbers
• Email addresses
• Google map address plugin for up to 3 locations

```html
<!DOCTYPE html>
<html lang="en">
<head>
<meta charset="utf-8">
<title>Brellmoor Aviation</title>
<link href="https://fonts.googleapis.com/css2?family=Raleway:wght@400;500;700&family=Open+Sans:wght@400;600&display=swap" rel="stylesheet">
<style>
  :root {
    --ink: #1d1d1d;
    --text: #444444;
    --muted: #555555;
    --accent: #3a9cf2;
    --accent-deep: #1f5a92;
    --button: #1b1b1b;
    --rule: #dcdcdc;
    --footer: #efefef;
    --white: #ffffff;
    --social-dark: #3b5a99;
    --social-light: #4aa8e6;
  }
  * { margin: 0; padding: 0; box-sizing: border-box; }
  html, body { width: 1200px; height: 1180px; overflow: hidden; background: var(--white); }
  body { position: relative; font-family: "Open Sans", sans-serif; color: var(--text); }

  .site-header { position: absolute; top: 0; left: 0; width: 1200px; height: 91px; }
  .brand { position: absolute; left: 199px; top: 30px; font-family: "Raleway", sans-serif; font-weight: 700; font-size: 30px; color: var(--ink); letter-spacing: 0.5px; }
  .main-nav a { position: absolute; top: 41px; font-family: "Raleway", sans-serif; font-weight: 500; font-size: 13.5px; color: #333; text-decoration: none; letter-spacing: 0.2px; }

  .hero { position: absolute; top: 91px; left: 0; width: 1200px; height: 469px;
    background: linear-gradient(180deg, #8ea3bd 0%, #b7c4d3 35%, #5d6a72 62%, #3c4043 75%, #9b8668 88%, #7f6c52 100%); }
  .hero-caption { position: absolute; left: 194px; top: 144px; width: 396px; height: 158px; background: var(--accent); opacity: 0.93; color: var(--white); padding: 28px 0 0 28px; }
  .hero-caption h1 { font-family: "Raleway", sans-serif; font-weight: 400; font-size: 32px; line-height: 1; letter-spacing: 0.5px; }
  .hero-caption h2 { font-family: "Raleway", sans-serif; font-weight: 500; font-size: 17.5px; margin-top: 10px; }
  .hero-caption p { font-size: 9.5px; line-height: 16px; margin-top: 10px; }
  .slider-dots { position: absolute; left: 563px; top: 437px; display: flex; gap: 6px; }
  .slider-dots span { width: 14px; height: 14px; border-radius: 50%; background: #3a3a3a; }

  .service { position: absolute; top: 600px; width: 190px; }
  .service-photo { width: 190px; height: 100px; }
  .service h3 { font-family: "Raleway", sans-serif; font-weight: 500; font-size: 14px; line-height: 16px; color: #333; margin-top: 11px; }
  .service p { font-size: 9.3px; line-height: 14px; color: var(--muted); margin-top: 3px; }
  .read-more { position: absolute; top: 191px; left: 0; width: 68px; height: 21px; background: var(--button); color: var(--white); font-size: 8.5px; line-height: 21px; text-align: center; }

  .divider { position: absolute; left: 197px; top: 865px; width: 806px; height: 1px; background: var(--rule); }

  .news-title { position: absolute; left: 198px; top: 898px; font-family: "Raleway", sans-serif; font-weight: 400; font-size: 21px; color: var(--ink); }
  .news-item { position: absolute; top: 939px; width: 260px; }
  .news-item h4 { font-family: "Raleway", sans-serif; font-weight: 500; font-size: 14px; color: var(--accent-deep); }
  .news-item p { font-size: 9.3px; line-height: 17.3px; color: var(--text); margin-top: 2px; }
  .news-item time { display: block; font-size: 9.3px; color: #222; margin-top: 3px; }

  .site-footer { position: absolute; top: 1077px; left: 0; width: 1200px; height: 103px; background: var(--footer); }
  .footer-nav { position: absolute; left: 198px; top: 31px; font-family: "Raleway", sans-serif; font-weight: 500; font-size: 12px; color: #222; }
  .footer-nav span { margin: 0 8px; }
  .copyright { position: absolute; left: 198px; top: 52px; font-size: 9.5px; color: var(--muted); }
  .social { position: absolute; left: 944px; top: 28px; display: flex; gap: 6px; }
  .social span { width: 20px; height: 20px; border-radius: 3px; }
  .social .social-first { background: var(--social-dark); }
  .social .social-second { background: var(--social-light); }
</style>
</head>
<body>
  <header class="site-header">
    <div class="brand">Brellmoor</div>
    <nav class="main-nav">
      <a style="left:548px">HOME</a>
      <a style="left:625px">ABOUT US</a>
      <a style="left:728px">NEWS</a>
      <a style="left:806px">SERVICES</a>
      <a style="left:905px">CONTACT US</a>
    </nav>
  </header>

  <section class="hero" role="img" aria-label="Twin-propeller aircraft on a runway with mountains and clouds behind">
    <div class="hero-caption">
      <h1>Sedmetus augue conva</h1>
      <h2>Etiam urna Sed porta Suspendisse</h2>
      <p>Vivamus porttitor purus nisi eleifend libero a tempus libero lectus feugiat felis<br>Morbi diam mauris viverra in gravida eu mattis in ante</p>
    </div>
    <div class="slider-dots"><span></span><span></span><span></span><span></span></div>
  </section>

  <article class="service" style="left:197px">
    <div class="service-photo" role="img" aria-label="Engineers servicing aircraft equipment" style="background:linear-gradient(135deg,#3f6fae,#1f3558)"></div>
    <h3>Aviation Engineering<br>Services</h3>
    <p>Vivamus porttitor purus nisi eleifend<br>libero a tempus libero lectus feugiat felis<br>Morbi diam mauris viverra</p>
    <div class="read-more">Read More</div>
  </article>
  <article class="service" style="left:401px">
    <div class="service-photo" role="img" aria-label="Engineers consulting beside machinery" style="background:linear-gradient(135deg,#9aa0a6,#3a4452)"></div>
    <h3>Aviation Consulting</h3>
    <p>Vivamus porttitor purus nisi eleifend<br>libero a tempus libero lectus feugiat felis<br>Morbi diam mauris viverra lit at tellus nec<br>ultricies sit a</p>
    <div class="read-more">Read More</div>
  </article>
  <article class="service" style="left:605px">
    <div class="service-photo" role="img" aria-label="Close view of a jet engine fan" style="background:linear-gradient(135deg,#5a6068,#1e2226)"></div>
    <h3>Aviation Equipment<br>Supplies</h3>
    <p>Vivamus porttitor purus nisi eleifend<br>libero a tempus libero lectus feugiat felis<br>Morbi diam mauris viverra</p>
    <div class="read-more">Read More</div>
  </article>
  <article class="service" style="left:810px">
    <div class="service-photo" role="img" aria-label="Aircraft engine on a workshop stand" style="background:linear-gradient(135deg,#4d6690,#a7b0b8)"></div>
    <h3>Aviation Construction<br>Projects</h3>
    <p>Vivamus porttitor purus nisi eleifend<br>libero a tempus libero lectus feugiat felis<br>Morbi diam mauris viverra</p>
    <div class="read-more">Read More</div>
  </article>

  <div class="divider"></div>

  <h2 class="news-title">LATEST NEWS</h2>
  <article class="news-item" style="left:199px">
    <h4>Morbi eget arcu Morbi porta</h4>
    <p>nonummy nibh ligula pulvinar metus eget consectetuer<br>augue nisi quis lacus Ut ac mi quis lacus mollis aliquam<br>Curabitur iaculis tempCurabitur vel mi</p>
    <time>on 25 Jan 2014</time>
  </article>
  <article class="news-item" style="left:479px">
    <h4>Fusce ultricies orci ac</h4>
    <p>nonummy nibh ligula pulvinar metus eget consectetuer<br>augue nisi quis lacus Ut ac mi quis lacus mollis aliquam<br>Curabitur iaculis tempCurabitur vel mi</p>
    <time>on 15 Jan 2014</time>
  </article>
  <article class="news-item" style="left:759px">
    <h4>Curabitur vel mi sit amet magna</h4>
    <p>nonummy nibh ligula pulvinar metus eget consectetuer<br>augue nisi quis lacus Ut ac mi quis lacus mollis aliquam<br>Curabitur iaculis tempCurabitur vel mi</p>
    <time>on 10 Jan 2014</time>
  </article>

  <footer class="site-footer">
    <nav class="footer-nav">HOME<span>|</span>ABOUT US<span>|</span>NEWS<span>|</span>SERVICES<span>|</span>CONTACT US</nav>
    <div class="copyright">© 2015 Company Name&nbsp; All right reserved&nbsp; Term of Use</div>
    <div class="social">
      <span class="social-first" aria-label="Social network link"></span>
      <span class="social-second" aria-label="Social network link"></span>
    </div>
  </footer>
</body>
</html>
```